Business card alterations

I have changed my business name from Brisa Laser Renewal Clinic to simply "Brisa Laser Clinic' and need this logo changed to reflect same

Brisa Laser Clinic
Est. 2004

I also need new business cards with above logo included and this attached card changed to the following.
Marcia Pellbrook
Dermal Aesthetician
Grad Cert in Laser & IPL Treatments

I need at least one logo in less than 4mb so I can upload into my newsletter format so I can upload to newsletters, emails etc

Thanks
Marcie

```html
<!DOCTYPE html>
<html lang="en">
<head>
<meta charset="utf-8">
<title>Brisa Laser Clinic – Business Card</title>
<link rel="stylesheet" href="https://fonts.googleapis.com/css2?family=Arimo:wght@400;700&display=swap">
<style>
  :root {
    --backdrop: #2f3b41;
    --card-green: #009a56;
    --ink-white: #ffffff;
    --shadow: rgba(0, 0, 0, 0.35);
  }
  * { box-sizing: border-box; margin: 0; padding: 0; }
  html, body {
    width: 1200px;
    height: 1000px;
    overflow: hidden;
    background: var(--backdrop);
    font-family: "Arimo", Arial, sans-serif;
    color: var(--ink-white);
  }
  .business-card {
    position: absolute;
    left: 100px;
    top: 194px;
    width: 1000px;
    height: 612px;
    background: var(--card-green);
    box-shadow: 0 18px 40px var(--shadow);
  }
  .brand-lockup {
    position: absolute;
    top: 92px;
    left: 0;
    width: 100%;
    text-align: center;
  }
  .brand-name {
    font-size: 76px;
    font-weight: 400;
    letter-spacing: 1px;
    line-height: 1;
  }
  .brand-established {
    margin-top: 22px;
    font-size: 24px;
    letter-spacing: 4px;
  }
  .person-details {
    position: absolute;
    right: 430px;
    top: 358px;
    text-align: right;
  }
  .person-name {
    font-size: 31px;
    font-weight: 700;
    margin-bottom: 10px;
  }
  .person-role {
    font-size: 23px;
    line-height: 31px;
  }
  .column-divider {
    position: absolute;
    left: 592px;
    top: 358px;
    width: 2px;
    height: 198px;
    background: var(--ink-white);
  }
  .contact-details {
    position: absolute;
    left: 620px;
    top: 356px;
    font-size: 25px;
    line-height: 37px;
    list-style: none;
  }
  .contact-phone { font-weight: 700; }
  .contact-phone .label { margin-right: 14px; }
</style>
</head>
<body>
  <section class="business-card" aria-label="Brisa Laser Clinic business card">
    <header class="brand-lockup">
      <div class="brand-name">Brisa Laser Clinic</div>
      <div class="brand-established">EST. 2004</div>
    </header>

    <div class="person-details">
      <div class="person-name">Marcia Pellbrook</div>
      <div class="person-role">Dermal Aesthetician</div>
      <div class="person-role">Grad Cert in Laser &amp; IPL Treatments</div>
    </div>

    <div class="column-divider"></div>

    <ul class="contact-details">
      <li class="contact-phone"><span class="label">T</span>(08) 8412 7305</li>
      <li>info@brisaclinic.com.au</li>
      <li>www.brisaclinic.com.au</li>
      <li>58 Kestrel Avenue</li>
      <li>Ashmore Vale SA 5071</li>
    </ul>
  </section>
</body>
</html>
```